Re-design of Business Card

We require a design for our business card.

Korrim is a supplier of industrial packaging specializing in plastic products. We are undergoing a rebranding to appear more corporate. We have changed our company name to korrim and have a new logo.

I have uploaded our old card design with the previous company name.
Don't copy the current design. We are looking for a new design.

Industry/Entity Type

Manufacturing

Contact Information for Business Card

please don't copy the current design. we are looking for a new design.

Font styles to use
Sans Serif

Colors

Designer to choose colors to be used in the design.

Requirements
Must have
• clean and easy to read.

```html
<!DOCTYPE html>
<html lang="en">
<head>
<meta charset="utf-8">
<title>Korrim Business Card</title>
<link href="https://fonts.googleapis.com/css2?family=Montserrat:wght@400;500;600;700&display=swap" rel="stylesheet">
<style>
  :root {
    --brand-orange: #f47b20;
    --paper-white: #ffffff;
    --ink-dark: #1e1e1e;
    --ink-muted: #8a8a8a;
    --backdrop: #e9e6e1;
  }
  * { margin: 0; padding: 0; box-sizing: border-box; }
  html, body {
    width: 1200px; height: 900px; overflow: hidden;
    background: var(--backdrop);
    font-family: "Montserrat", sans-serif;
  }
  .stage { position: relative; width: 1200px; height: 900px; }
  .card {
    position: absolute; left: 311px; width: 577px; height: 329px;
    box-shadow: 0 8px 18px rgba(0,0,0,0.18);
  }
  .card-front { top: 98px; background: var(--brand-orange); color: var(--paper-white); }
  .card-back { top: 472px; background: var(--paper-white); color: var(--ink-dark); }

  .front-wordmark {
    position: absolute; left: 0; right: 0; top: 116px;
    display: flex; justify-content: center; align-items: center; gap: 14px;
    font-weight: 700; font-size: 56px; letter-spacing: 1px; line-height: 1;
  }
  .front-wordmark .mark-square { width: 22px; height: 22px; background: var(--paper-white); }
  .services {
    position: absolute; left: 0; right: 0; top: 194px;
    text-align: center; font-weight: 500; font-size: 14.5px; line-height: 20px;
    letter-spacing: 0.3px; text-transform: uppercase;
  }

  .person-name {
    position: absolute; left: 31px; top: 30px;
    color: var(--brand-orange); font-weight: 700; font-size: 18.5px; letter-spacing: 0.4px;
  }
  .person-title {
    position: absolute; left: 31px; top: 51px;
    color: var(--ink-muted); font-size: 14.5px;
  }
  .contact-list { position: absolute; left: 31px; list-style: none; }
  .contact-list li {
    display: flex; align-items: center; gap: 8px;
    height: 22px; font-size: 15px; font-weight: 500;
  }
  .contact-list svg { width: 15px; height: 15px; fill: var(--brand-orange); flex: none; }
  .contact-personal { top: 74px; }
  .contact-office { top: 188px; }

  .back-wordmark {
    position: absolute; right: 33px; top: 50px;
    display: flex; align-items: center; gap: 10px;
    color: var(--brand-orange); font-weight: 700; font-size: 38px; line-height: 1;
  }
  .back-wordmark .mark-square { width: 16px; height: 16px; background: var(--brand-orange); }

  .office-heading {
    position: absolute; left: 31px; right: 33px; top: 164px;
    display: flex; align-items: center; gap: 10px;
    color: var(--brand-orange); font-weight: 700; font-size: 15.5px;
  }
  .office-heading::after { content: ""; flex: 1; height: 2px; background: var(--brand-orange); }

  .office-address {
    position: absolute; right: 32px; top: 188px;
    text-align: right; font-style: normal; font-size: 15px; font-weight: 500; line-height: 22px;
  }
  .credentials-band {
    position: absolute; left: 0; right: 0; bottom: 0; height: 49px;
    background: var(--brand-orange); color: var(--paper-white);
    display: flex; align-items: center; justify-content: center;
    font-size: 14.5px; font-weight: 500;
  }
</style>
</head>
<body>
<main class="stage">
  <section class="card card-front">
    <div class="front-wordmark"><span class="mark-square"></span><span>KORRIM</span></div>
    <p class="services">Pallet Containment &nbsp;|&nbsp; Flexible Packaging<br>Pallet Wrapping Machinery &nbsp;|&nbsp; General Packaging</p>
  </section>

  <section class="card card-back">
    <h1 class="person-name">DANA WHITLOCK</h1>
    <p class="person-title">Machinery Sales Manager</p>
    <ul class="contact-list contact-personal">
      <li><svg viewBox="0 0 24 24"><path d="M6.6 10.8a15.1 15.1 0 0 0 6.6 6.6l2.2-2.2c.3-.3.7-.4 1-.2 1.1.4 2.3.6 3.6.6.6 0 1 .4 1 1V20c0 .6-.4 1-1 1C10.6 21 3 13.4 3 4c0-.6.4-1 1-1h3.5c.6 0 1 .4 1 1 0 1.3.2 2.5.6 3.6.1.3 0 .7-.2 1l-2.3 2.2z"/></svg>12 345 6780</li>
      <li><svg viewBox="0 0 24 24"><path d="M2 5h20v2l-10 6L2 7z M2 9l10 6 10-6v10H2z"/></svg>dana@korrim.com.au</li>
    </ul>

    <div class="back-wordmark"><span class="mark-square"></span><span>KORRIM</span></div>

    <h2 class="office-heading">HEAD OFFICE</h2>
    <ul class="contact-list contact-office">
      <li><svg viewBox="0 0 24 24"><path d="M6.6 10.8a15.1 15.1 0 0 0 6.6 6.6l2.2-2.2c.3-.3.7-.4 1-.2 1.1.4 2.3.6 3.6.6.6 0 1 .4 1 1V20c0 .6-.4 1-1 1C10.6 21 3 13.4 3 4c0-.6.4-1 1-1h3.5c.6 0 1 .4 1 1 0 1.3.2 2.5.6 3.6.1.3 0 .7-.2 1l-2.3 2.2z"/></svg>1300 555 014</li>
      <li><svg viewBox="0 0 24 24"><path d="M6 2h12v5H6z M3 8h18v9h-3v5H6v-5H3z M8 14v6h8v-6z"/></svg>+61 7 5550 1427</li>
      <li><svg viewBox="0 0 24 24"><path d="M12 2a10 10 0 1 0 0 20 10 10 0 0 0 0-20zm-1 17.9A8 8 0 0 1 4.2 10L9 15v1a2 2 0 0 0 2 2zm6.9-2.5A2 2 0 0 0 16 16h-1v-3a1 1 0 0 0-1-1H8v-2h2a1 1 0 0 0 1-1V7h2a2 2 0 0 0 2-2v-.4a8 8 0 0 1 2.9 12.8z"/></svg>www.korrim.com.au</li>
    </ul>
    <address class="office-address">48 Harlow Street<br>Marlowe Park, Qld<br>4199 Australia</address>

    <footer class="credentials-band">Distribution Throughout AUS &amp; NZ | HACCP Certified | ISO 9001</footer>
  </section>
</main>
</body>
</html>
```